Spiritual Healing bussiness needs logo/business card

Simple, clean looking logo/card
For spiritual business with healing services and occult rituals

Contact Information for Business Card

Needs my name: Corwin Halley
Business name: Veyra Healing Shop
Services provided and worded in this way:

Reiki Healing
Tarot
Oils
Rituals Of Change

Can look occult like but with light energy.

Colors
0255a3
3276b5
85abd2
33a6d7
85cae6
0292cd

```html
<!DOCTYPE html>
<html lang="en">
<head>
<meta charset="utf-8">
<title>Veyra Healing Shop – Business Card</title>
<link href="https://fonts.googleapis.com/css2?family=Cinzel:wght@400;500&family=Open+Sans:wght@400&display=swap" rel="stylesheet">
<style>
  :root {
    --navy: #0255a3;
    --mid-blue: #3276b5;
    --pale-blue: #85abd2;
    --sky: #33a6d7;
    --light-sky: #85cae6;
    --cyan: #0292cd;
    --paper: #f4f4f2;
    --ink: #222222;
    --stage-light: #e2e2e2;
    --stage-dark: #6e6e6e;
  }
  * { margin: 0; padding: 0; box-sizing: border-box; }
  html, body { width: 1200px; height: 900px; overflow: hidden; }
  body {
    position: relative;
    background: radial-gradient(ellipse at 45% 40%, var(--stage-light) 0%, #b4b4b4 55%, var(--stage-dark) 100%);
    font-family: "Cinzel", serif;
  }
  .card {
    position: absolute;
    width: 540px;
    height: 310px;
    border-radius: 24px;
    overflow: hidden;
    box-shadow: 0 10px 24px rgba(0,0,0,0.35);
  }
  /* Front card */
  .card-front {
    left: 70px; top: 90px;
    background: linear-gradient(160deg, var(--sky) 0%, var(--cyan) 45%, var(--navy) 100%);
    color: #ffffff;
  }
  .front-halo {
    position: absolute;
    left: 120px; top: 5px;
    width: 300px; height: 300px;
    border-radius: 50%;
    background: radial-gradient(circle, rgba(133,202,230,0.18) 0%, rgba(133,202,230,0.08) 55%, rgba(133,202,230,0) 72%);
  }
  .wordmark {
    position: absolute;
    display: flex;
    flex-direction: column;
    align-items: center;
  }
  .wordmark-name { font-weight: 400; line-height: 1; letter-spacing: 0.04em; }
  .wordmark-sub { letter-spacing: 0.55em; line-height: 1; margin-right: -0.55em; }
  .card-front .wordmark { left: 0; right: 0; top: 88px; }
  .card-front .wordmark-name { font-size: 72px; }
  .card-front .wordmark-sub { font-size: 15px; margin-top: 10px; }
  .services {
    position: absolute;
    left: 0; right: 0; bottom: 40px;
    text-align: center;
    font-size: 15px;
    letter-spacing: 0.04em;
  }
  .services .sep { margin: 0 12px; }

  /* Back card */
  .card-back {
    left: 590px; top: 420px;
    background: var(--paper);
    color: var(--navy);
  }
  .card-back .wordmark { left: 40px; width: 260px; top: 132px; }
  .card-back .wordmark-name { font-size: 54px; }
  .card-back .wordmark-sub { font-size: 12px; margin-top: 8px; color: var(--ink); }
  .contact {
    position: absolute;
    left: 330px; top: 104px;
    color: var(--ink);
  }
  .contact-name { font-size: 22px; margin-bottom: 14px; }
  .contact-line {
    display: flex; align-items: center; gap: 8px;
    font-family: "Open Sans", sans-serif;
    font-size: 13px;
    margin-bottom: 6px;
  }
  .contact-line svg { width: 14px; height: 14px; fill: var(--navy); }

  /* Standalone lockup */
  .lockup {
    left: 52px; top: 712px;
    color: var(--navy);
  }
  .lockup .wordmark-name { font-size: 104px; }
  .lockup .wordmark-sub { font-size: 26px; margin-top: 10px; color: #2a2a2a; letter-spacing: 0.42em; margin-right: -0.42em; }
</style>
</head>
<body>

<section class="card card-front">
  <div class="front-halo" role="img" aria-label="Faint geometric sacred-circle pattern behind the name"></div>
  <div class="wordmark">
    <span class="wordmark-name">VEYRA</span>
    <span class="wordmark-sub">HEALING SHOP</span>
  </div>
  <p class="services">Reiki Healing<span class="sep">|</span>Tarot<span class="sep">|</span>Oils<span class="sep">|</span>Rituals Of Change</p>
</section>

<section class="card card-back">
  <div class="wordmark">
    <span class="wordmark-name">VEYRA</span>
    <span class="wordmark-sub">HEALING SHOP</span>
  </div>
  <div class="contact">
    <p class="contact-name">Corwin Halley</p>
    <p class="contact-line">
      <svg viewBox="0 0 16 16" aria-hidden="true"><path d="M3 1.5l2.5 0 1.2 3.2-1.6 1.2c.8 1.8 2.2 3.2 4 4l1.2-1.6 3.2 1.2v2.5c0 .8-.7 1.5-1.5 1.5C6.6 13.5 2.5 9.4 1.5 3c0-.8.7-1.5 1.5-1.5z"/></svg>
      000 000 0000
    </p>
    <p class="contact-line">
      <svg viewBox="0 0 16 16" aria-hidden="true"><path d="M1 3h14v10H1z M1.8 3.8L8 8.6l6.2-4.8" fill="none" stroke="#0255a3" stroke-width="1.6"/></svg>
      youremail@xyz.com
    </p>
  </div>
</section>

<div class="wordmark lockup">
  <span class="wordmark-name">VEYRA</span>
  <span class="wordmark-sub">HEALING SHOP</span>
</div>

</body>
</html>
```